New modern business card design

To design a brand new business card that's clean & modern in terms of layout.
I have attached our company logo and also basic information regarding what is needed on the card that also needs to be editable.

Target Market(s)

motor trade

Contact Information for Business Card

logo, name, title, tel, mob, email, address, www, all information is in the word.doc file

Requirements
Must have
• white background
Nice to have
• Nice clean font

```html
<!DOCTYPE html>
<html lang="en">
<head>
<meta charset="utf-8">
<title>Boltworks Ltd – Business Card</title>
<link href="https://fonts.googleapis.com/css2?family=Open+Sans:wght@400;600;700&display=swap" rel="stylesheet">
<style>
  :root {
    --page-bg: #e8e9eb;
    --card-bg: #ffffff;
    --brand-blue: #2f7fc8;
    --rule-blue: #5a9bd6;
    --text-grey: #a3a6aa;
    --shadow: rgba(0, 0, 0, 0.12);
  }
  html, body {
    margin: 0;
    width: 1200px;
    height: 1200px;
    overflow: hidden;
    background: var(--page-bg);
    font-family: "Open Sans", Arial, sans-serif;
  }
  .stage {
    width: 1200px;
    height: 1200px;
    display: flex;
    align-items: center;
    justify-content: center;
  }
  .business-card {
    position: relative;
    width: 960px;
    height: 644px;
    background: var(--card-bg);
    box-shadow: 0 18px 50px var(--shadow);
  }
  .brand {
    position: absolute;
    top: 120px;
    left: 0;
    right: 0;
    display: flex;
    align-items: center;
    justify-content: center;
    gap: 18px;
  }
  .brand-square {
    width: 34px;
    height: 34px;
    background: var(--brand-blue);
  }
  .brand-name {
    font-size: 46px;
    font-weight: 600;
    color: var(--brand-blue);
    letter-spacing: 1px;
  }
  .divider {
    position: absolute;
    top: 236px;
    left: 98px;
    width: 773px;
    height: 2px;
    background: var(--rule-blue);
  }
  .contact-person {
    position: absolute;
    top: 318px;
    left: 98px;
  }
  .person-name {
    margin: 0 0 8px;
    font-size: 37px;
    font-weight: 700;
    color: var(--brand-blue);
  }
  .person-detail {
    margin: 0;
    font-size: 25px;
    line-height: 37px;
    color: var(--text-grey);
  }
  .address {
    position: absolute;
    top: 318px;
    right: 89px;
    margin: 0;
    font-style: normal;
    text-align: right;
    font-size: 25px;
    line-height: 37px;
    color: var(--text-grey);
  }
  .website {
    position: absolute;
    top: 525px;
    left: 0;
    right: 0;
    text-align: center;
    font-size: 36px;
    font-weight: 700;
    color: var(--brand-blue);
  }
</style>
</head>
<body>
  <main class="stage">
    <section class="business-card">
      <div class="brand">
        <span class="brand-square"></span>
        <span class="brand-name">BOLTWORKS LTD</span>
      </div>
      <div class="divider"></div>
      <div class="contact-person">
        <p class="person-name">Daniel Harper</p>
        <p class="person-detail">General Manager</p>
        <p class="person-detail">T: 0161 555 0142</p>
        <p class="person-detail">M: 07700900518</p>
      </div>
      <address class="address">
        Linden Road<br>
        Ashwell<br>
        Northbury<br>
        NB4 2QT
      </address>
      <div class="website">www.boltworks-ltd.co.uk</div>
    </section>
  </main>
</body>
</html>
```